Ridge Contracting LLC Business Card Design

I am looking for a creative and unique business card design. We are a commercial construction general contractor. With the name "RIDGE" Contracting, I am hoping to see some neat designs that correlate with the name.

```html
<!DOCTYPE html>
<html lang="en">
<head>
<meta charset="utf-8">
<title>Ridge Contracting LLC – Business Card</title>
<link rel="stylesheet" href="https://fonts.googleapis.com/css2?family=Roboto:wght@400;500;700&family=Exo+2:wght@700&display=swap">
<style>
  :root {
    --page-bg: #2b2b2c;
    --card-dark: #1f2022;
    --card-dark-edge: #2a2b2e;
    --card-light: #f1f1f1;
    --card-light-edge: #e2e2e2;
    --brand-blue: #2c84c6;
    --brand-blue-deep: #2470b0;
    --band-rule: #b8bcc0;
    --logo-grey: #8a8c90;
    --text-light: #e6e6e6;
    --text-dark: #3a3a3a;
    --white: #ffffff;
  }
  * { box-sizing: border-box; margin: 0; padding: 0; }
  html, body { width: 1200px; height: 1138px; overflow: hidden; }
  body {
    background: var(--page-bg);
    font-family: "Roboto", sans-serif;
    position: relative;
  }
  .card {
    position: absolute;
    border-radius: 16px;
    overflow: hidden;
  }
  .card--front {
    left: 274px; top: 186px; width: 623px; height: 376px;
    background: linear-gradient(160deg, var(--card-dark) 0%, var(--card-dark-edge) 100%);
  }
  .card--back {
    left: 276px; top: 608px; width: 618px; height: 374px;
    background: linear-gradient(180deg, var(--card-light) 0%, var(--card-light-edge) 100%);
  }
  .brand-name {
    position: absolute;
    left: 0; right: 0;
    text-align: center;
    font-family: "Exo 2", sans-serif;
    font-weight: 700;
    letter-spacing: 2px;
    white-space: nowrap;
  }
  .card--front .brand-name {
    top: 150px;
    font-size: 40px;
    color: #5c5e62;
  }
  .card--back .brand-name {
    top: 82px;
    font-size: 40px;
    color: var(--brand-blue);
  }
  .brand-name .mark-dot {
    display: inline-block;
    width: 16px; height: 16px;
    border-radius: 50%;
    background: currentColor;
    margin-right: 14px;
    vertical-align: 4px;
  }
  .legal-line {
    position: absolute;
    top: 331px; left: 0; right: 0;
    display: flex; justify-content: center; align-items: center;
    gap: 18px;
    color: var(--text-light);
    font-size: 16px;
  }
  .legal-line .rule {
    width: 70px; height: 2px;
    background: var(--brand-blue);
  }
  .contact-band {
    position: absolute;
    left: 0; right: 0; top: 202px; height: 106px;
    background: linear-gradient(90deg, var(--brand-blue-deep) 0%, var(--brand-blue) 55%, var(--brand-blue-deep) 100%);
    border-top: 3px solid var(--band-rule);
    border-bottom: 3px solid var(--band-rule);
  }
  .person {
    position: absolute;
    right: 345px; top: 26px;
    text-align: right;
    color: var(--white);
  }
  .person__name {
    font-family: "Exo 2", sans-serif;
    font-weight: 700;
    font-size: 27px;
    letter-spacing: 0.5px;
    line-height: 1.1;
  }
  .person__title {
    font-size: 15.5px;
    margin-top: 4px;
    color: #e4eef7;
  }
  .contact-list {
    position: absolute;
    left: 305px; top: 17px;
    list-style: none;
    color: var(--white);
    font-size: 16px;
  }
  .contact-list li {
    display: flex; align-items: center;
    height: 23.5px;
  }
  .contact-list svg {
    width: 14px; height: 14px;
    margin-right: 18px;
    fill: #dfe8f2;
  }
  .address {
    position: absolute;
    left: 0; right: 0; top: 327px;
    text-align: center;
    font-size: 16px;
    color: var(--text-dark);
  }
</style>
</head>
<body>

<section class="card card--front" aria-label="Card front">
  <div class="brand-name"><span class="mark-dot"></span>RIDGE CONTRACTING</div>
  <p class="legal-line"><span class="rule"></span>Ridge Contracting LLC<span class="rule"></span></p>
</section>

<section class="card card--back" aria-label="Card back">
  <div class="brand-name"><span class="mark-dot"></span>RIDGE CONTRACTING</div>

  <div class="contact-band">
    <div class="person">
      <p class="person__name">MARCUS HALE</p>
      <p class="person__title">Managing Director</p>
    </div>
    <ul class="contact-list">
      <li>
        <svg viewBox="0 0 16 16" aria-hidden="true"><path d="M1 5c0-2 3-3 7-3s7 1 7 3v1.5h-3.5V5h-7v1.5H1z"/><rect x="3" y="7.5" width="10" height="6.5" rx="1"/></svg>
        828-555-0142
      </li>
      <li>
        <svg viewBox="0 0 16 16" aria-hidden="true"><path d="M1 3h14v10H1z M2 4l6 5 6-5" fill="none" stroke="#dfe8f2" stroke-width="1.6"/></svg>
        marcus@ridgecontracting.com
      </li>
      <li>
        <svg viewBox="0 0 16 16" aria-hidden="true"><circle cx="8" cy="8" r="6.5" fill="none" stroke="#dfe8f2" stroke-width="1.4"/><path d="M1.5 8h13M8 1.5c-3 3.5-3 9.5 0 13M8 1.5c3 3.5 3 9.5 0 13" fill="none" stroke="#dfe8f2" stroke-width="1.2"/></svg>
        www.ridgecontracting.com
      </li>
    </ul>
  </div>

  <p class="address">118 Summit Ave., Cedar Falls, NC 28801</p>
</section>

</body>
</html>
```